Google Form Graphic to suit our Brand and industry

Create a graphic / image for us to put at the top of our client enquiry google form.
The image will be a section of an architectural home with our branding over the top. Preferably translucent.
The image must suit the shape of the google forms image, which is an elongated rectangle
#003d5d - brand colour

Target Market(s)

residential home owners, high end architectural homes

Industry/Entity Type

Residential construction

Colors
0054AA
0677BA
7BADD7
CADEEF
E8F1F8

Requirements
Must have
• our branding and a photo of an architectural home in the background

```html
<!DOCTYPE html>
<html lang="en">
<head>
<meta charset="utf-8">
<title>New Client Enquiry Form – Norta Build</title>
<link rel="stylesheet" href="https://fonts.googleapis.com/css2?family=Roboto:wght@400;500&display=swap">
<style>
  :root {
    --page-bg: #f6efdf;
    --card-bg: #ffffff;
    --card-border: #dcdcdc;
    --brand-navy: #003d5d;
    --photo-light: #cfd2d4;
    --photo-mid: #7f868b;
    --text-main: #202124;
    --text-muted: #70757a;
    --rule-gold: #7d6a45;
    --focus-blue: #4285f4;
    --required-red: #d93025;
    --badge-gold: #e4bb62;
    --brand-ink: #ffffff;
  }
  * { box-sizing: border-box; margin: 0; padding: 0; }
  html, body { width: 862px; height: 1200px; overflow: hidden; }
  body {
    position: relative;
    background: var(--page-bg);
    font-family: "Roboto", Arial, sans-serif;
    color: var(--text-main);
  }
  .header-banner {
    position: absolute; left: 32px; top: 13px; width: 797px; height: 198px;
    border-radius: 8px; overflow: hidden;
    background: linear-gradient(90deg, var(--photo-light) 0%, var(--photo-mid) 40%, #1d4d68 70%, var(--brand-navy) 100%);
  }
  .brand-name {
    position: absolute; right: 48px; bottom: 34px;
    font-family: "Roboto", Arial, sans-serif; font-weight: 400;
    font-size: 30px; line-height: 1;
    color: var(--brand-ink); white-space: nowrap;
  }
  .card {
    position: absolute; left: 34px; width: 790px;
    background: var(--card-bg); border: 1px solid var(--card-border); border-radius: 8px;
  }
  .form-title-card { top: 272px; height: 171px; border-radius: 0 0 8px 8px; }
  .form-title {
    position: absolute; left: 25px; top: 24px;
    font-size: 32px; font-weight: 400; line-height: 1.2; color: var(--text-main);
  }
  .title-rule { position: absolute; left: 25px; top: 70px; width: 654px; height: 1.5px; background: var(--rule-gold); }
  .card-tools { position: absolute; left: 698px; top: 26px; display: flex; gap: 36px; }
  .toolbar { position: absolute; left: 38px; top: 82px; display: flex; gap: 22px; align-items: center; }
  .toolbar svg { display: block; }
  .form-description { position: absolute; left: 25px; top: 123px; font-size: 14.5px; color: var(--text-main); }
  .question-card { height: 141px; }
  .question-card.is-active { border-left: 5px solid var(--focus-blue); }
  .question-label { position: absolute; left: 25px; top: 22px; font-size: 16px; }
  .is-active .question-label { left: 28px; }
  .required { color: var(--required-red); margin-left: 10px; }
  .answer-placeholder { position: absolute; left: 25px; top: 74px; font-size: 13px; color: var(--text-muted); letter-spacing: 0.3px; }
  .is-active .answer-placeholder { left: 20px; }
  .answer-line { position: absolute; left: 25px; top: 91px; width: 371px; border-top: 1px dotted #9aa0a6; }
  .is-active .answer-line { left: 20px; }
  .q-source { top: 458px; }
  .q-name { top: 613px; }
  .q-phone { top: 769px; }
  .q-email { top: 924px; }
  .section-routing { position: absolute; top: 1085px; left: 33px; font-size: 13.5px; color: #3c4043; display: flex; }
  .section-routing .route-choice { margin-left: 18px; width: 310px; }
  .section-routing svg { margin-top: 5px; }
  .side-rule { position: absolute; left: 835px; top: 1087px; width: 1px; height: 113px; background: #cfc8b8; }
  .section-badge {
    position: absolute; left: 33px; top: 1164px; width: 124px; height: 44px;
    background: var(--badge-gold); border-radius: 8px 8px 0 0;
    font-size: 13.5px; color: #3a2f16; padding: 10px 0 0 17px;
  }
</style>
</head>
<body>
  <header class="header-banner" role="img" aria-label="Photograph of a modern architectural home with large glazed walls, toned in brand navy">
    <div class="brand-name">Norta Build</div>
  </header>

  <section class="card form-title-card">
    <h1 class="form-title">New Client Enquiry Form</h1>
    <div class="title-rule"></div>
    <div class="card-tools" aria-hidden="true">
      <svg width="14" height="20" viewBox="0 0 14 20"><path d="M3 2l4 4 4-4M3 18l4-4 4 4" stroke="#5f6368" stroke-width="1.8" fill="none"/></svg>
      <svg width="6" height="20" viewBox="0 0 6 20"><circle cx="3" cy="3" r="2" fill="#5f6368"/><circle cx="3" cy="10" r="2" fill="#5f6368"/><circle cx="3" cy="17" r="2" fill="#5f6368"/></svg>
    </div>
    <div class="toolbar" aria-hidden="true">
      <svg width="18" height="18" viewBox="0 0 18 18"><text x="3" y="15" font-family="Roboto, sans-serif" font-weight="700" font-size="16" fill="#444">B</text></svg>
      <svg width="18" height="18" viewBox="0 0 18 18"><path d="M7 3h7M4 15h7M11 3L7 15" stroke="#444" stroke-width="1.8" fill="none"/></svg>
      <svg width="18" height="20" viewBox="0 0 18 20"><path d="M4 2v7a5 5 0 0 0 10 0V2M3 18h12" stroke="#444" stroke-width="1.6" fill="none"/></svg>
      <svg width="22" height="18" viewBox="0 0 22 18"><rect x="1.5" y="5" width="10" height="8" rx="4" stroke="#444" stroke-width="1.6" fill="none"/><rect x="10.5" y="5" width="10" height="8" rx="4" stroke="#444" stroke-width="1.6" fill="none"/></svg>
      <svg width="20" height="20" viewBox="0 0 20 20"><path d="M3 3h14M10 3l-3 15M4 9l12 10" stroke="#444" stroke-width="1.6" fill="none"/></svg>
    </div>
    <p class="form-description">We would love to hear your thoughts or feedback on how we can improve your experience!</p>
  </section>

  <section class="card question-card is-active q-source">
    <p class="question-label">Firstly, how did you hear about us?<span class="required">*</span></p>
    <p class="answer-placeholder">Short answer text</p>
    <div class="answer-line"></div>
  </section>

  <section class="card question-card q-name">
    <p class="question-label">Name</p>
    <p class="answer-placeholder">Short answer text</p>
    <div class="answer-line"></div>
  </section>

  <section class="card question-card q-phone">
    <p class="question-label">Phone</p>
    <p class="answer-placeholder">Short answer text</p>
    <div class="answer-line"></div>
  </section>

  <section class="card question-card q-email">
    <p class="question-label">Email</p>
    <p class="answer-placeholder">Short answer text</p>
    <div class="answer-line"></div>
  </section>

  <div class="section-routing">
    <span>After section 1</span>
    <span class="route-choice">Continue to next section</span>
    <svg width="10" height="6" viewBox="0 0 10 6" aria-hidden="true"><path d="M0 0h10L5 5z" fill="#5f6368"/></svg>
  </div>
  <div class="side-rule"></div>

  <div class="section-badge">Section 2 of 4</div>
</body>
</html>
```